Exterior cleaning company requires a eye catching a5 leaflet

we need some updated leaflet designs, a5 folded, we are targeting all exterior cleaning contracts, including roof cleaning & treatment, render cleaning & Treatment, driveways, block paving cleaning using the latest in low pressure cleaning technologies along side high pressure jetwashing. gutter clearance and flushing, water fed telescopic pole window cleaning of difficult to reach windows and high buildings. our website : www.tkbellowsec.co.uk facebook page: https://www.facebook.com/tkbellowsexteriorcareltd Instagram: https://www.instagram.com/tkbellowsec/ a quick google search of roof cleaning, soft washing etc will provide results of what we are doing

Target Market(s)

home owners, commercial clients

Font styles to use
Serif
Sans Serif

Requirements
Must have
• A5 Landscape folded leaflet, front page with company information and bullet points of main works : window & conservatory cleaning, roof cleaning & treatment, Render cleaning & treatment, pressure washing, soft washing, gutter clearing, pressure washing of patios, driveways, gutters, fascias (more info can be provided on techniques etc if required)

```html
<!DOCTYPE html>
<html lang="en">
<head>
<meta charset="utf-8">
<title>TK Bellows Exterior Care – A5 Leaflet</title>
<link href="https://fonts.googleapis.com/css2?family=Roboto+Condensed:wght@400;500;700&family=Roboto:wght@400;500;700&display=swap" rel="stylesheet">
<style>
  :root{
    --bg:#dcdcdf;
    --paper:#ffffff;
    --panel:#f0f0f0;
    --ink:#2b2b2b;
    --ink-soft:#5a5a5a;
    --rule:#9a9a9a;
  }
  *{box-sizing:border-box;margin:0;padding:0}
  html,body{width:1200px;height:3600px;overflow:hidden}
  body{background:var(--bg);font-family:"Roboto",sans-serif;color:var(--ink);position:relative}

  .scene{position:absolute;left:0;width:1200px;height:900px}
  .scene--front{top:0}
  .scene--outer{top:900px}
  .scene--inner{top:1800px}
  .scene--back{top:2700px}

  .page{position:relative;width:960px;height:679px;background:var(--paper);box-shadow:0 6px 18px rgba(0,0,0,.12);overflow:hidden}
  .scene > .page{position:absolute;left:120px;top:110px}

  .spread{position:absolute;left:40px;top:252px;width:1120px;height:396px;display:flex;box-shadow:0 6px 18px rgba(0,0,0,.12)}
  .spread__slot{width:560px;height:396px;overflow:hidden;position:relative}
  .spread__slot .page{transform:scale(.58333);transform-origin:0 0;box-shadow:none}

  /* brand */
  .brand{position:absolute;display:flex;align-items:center;gap:14px}
  .brand__mark{width:54px;height:54px;border:2px solid var(--ink);border-radius:50%;flex:none}
  .brand__name{font-family:"Roboto Condensed",sans-serif;font-weight:700;font-size:26px;line-height:1;color:var(--ink)}
  .brand__sub{font-size:12px;color:var(--ink-soft);margin-top:4px}
  .brand__tel{font-size:12px;font-weight:700;color:var(--ink);margin-top:2px}

  /* photo placeholders */
  .photo{position:absolute}
  .photo--shopfront{background:linear-gradient(135deg,#6f7a80 0%,#3b4349 35%,#5c8a3a 60%,#c8b05a 80%,#3a3f44 100%)}
  .photo--townhouse{background:linear-gradient(160deg,#8a4a38 0%,#6e3a2c 50%,#4f6a3a 100%)}
  .photo--glass{background:linear-gradient(180deg,#7f858a 0%,#3d4246 55%,#5b5a52 100%)}
  .photo--office{background:linear-gradient(160deg,#b9c2cc 0%,#e6e6e2 45%,#3f4246 100%)}
  .photo--interior{background:linear-gradient(140deg,#3a2a22 0%,#8a6a4a 45%,#d8c0a0 70%,#4a3a30 100%)}
  .photo--van{background:linear-gradient(160deg,#9aa3aa 0%,#f2f2f2 50%,#5d6268 100%)}
  .photo--van-dark{background:linear-gradient(160deg,#7e868c 0%,#4b5156 55%,#2f3337 100%)}
  .photo--facade{background:linear-gradient(150deg,#2f3236 0%,#4a4e52 50%,#6a5a40 100%)}

  /* front cover */
  .front .brand{left:70px;top:48px}
  .headline{position:absolute;left:470px;right:60px;top:52px;font-family:"Roboto Condensed",sans-serif;font-weight:500;font-size:22px;line-height:1.22;text-transform:uppercase;color:var(--ink)}
  .front .photo--shopfront{left:70px;top:150px;width:480px;height:370px}
  .services{position:absolute;left:550px;top:150px;width:340px;height:300px;background:var(--panel);padding:26px 28px}
  .section-title{font-family:"Roboto Condensed",sans-serif;font-weight:500;font-size:18px;text-transform:uppercase;color:var(--ink);padding-bottom:6px;border-bottom:1px solid var(--rule);display:inline-block;padding-right:90px}
  .services__list{list-style:none;margin-top:14px}
  .services__list li{font-size:13.5px;line-height:1.62;display:flex;align-items:center;gap:9px}
  .services__list li::before{content:"";width:7px;height:7px;border:1px solid var(--ink-soft);border-radius:50%;flex:none}

  .contact{position:absolute;left:0;right:0;top:578px;display:flex;justify-content:center;gap:70px;font-size:14px;font-weight:500}
  .contact__item{display:flex;align-items:center;gap:8px}
  .contact__item svg{width:14px;height:14px;fill:var(--ink)}

  /* back cover */
  .back .photo--townhouse{left:80px;top:110px;width:260px;height:210px}
  .back .photo--glass{left:350px;top:110px;width:260px;height:210px}
  .back .photo--office{left:620px;top:110px;width:260px;height:210px}
  .back .brand{left:375px;top:385px}

  /* inner pages */
  .about .photo--interior{left:50px;top:120px;width:420px;height:340px}
  .about .section-title,.detail .section-title{position:absolute}
  .about .section-title{left:500px;top:110px}
  .body-copy{position:absolute;font-size:12.5px;line-height:1.55;color:var(--ink-soft);text-align:justify}
  .body-copy p+p{margin-top:12px}
  .about .body-copy--col{left:500px;top:160px;width:410px}
  .about .body-copy--wide{left:50px;top:510px;width:860px}
  .detail .section-title{left:50px;top:80px}
  .detail .body-copy--col{left:50px;top:130px;width:400px}
  .detail .photo--van{left:50px;top:440px;width:195px;height:130px}
  .detail .photo--van-dark{left:255px;top:440px;width:195px;height:130px}
  .detail .photo--facade{left:490px;top:0;width:470px;height:679px}
</style>
</head>
<body>

<!-- front cover -->
<section class="scene scene--front">
  <article class="page front">
    <div class="brand">
      <span class="brand__mark"></span>
      <div><div class="brand__name">TK Bellows</div><div class="brand__sub">Exterior Care Ltd</div><div class="brand__tel">Tel: 01632 960 418</div></div>
    </div>
    <h1 class="headline">T.K Bellows Exterior Care is Southport's most reliable, professional cleaning company</h1>
    <div class="photo photo--shopfront" role="img" aria-label="Operative cleaning the glass frontage of a shop with a water fed pole"></div>
    <div class="services">
      <h2 class="section-title">Our services</h2>
      <ul class="services__list">
        <li>Window &amp; conservatory cleaning</li>
        <li>Roof cleaning &amp; treatment</li>
        <li>Render cleaning &amp; treatment</li>
        <li>Pressure washing</li>
        <li>Soft washing</li>
        <li>Gutter clearing</li>
        <li>Pressure washing of patios</li>
        <li>Driveways</li>
        <li>Gutters</li>
        <li>Fascias</li>
      </ul>
    </div>
    <div class="contact">
      <span class="contact__item"><svg viewBox="0 0 24 24"><path d="M6.6 10.8a15 15 0 0 0 6.6 6.6l2.2-2.2a1 1 0 0 1 1-.25 11.4 11.4 0 0 0 3.6.57 1 1 0 0 1 1 1V20a1 1 0 0 1-1 1A17 17 0 0 1 3 4a1 1 0 0 1 1-1h3.5a1 1 0 0 1 1 1c0 1.25.2 2.45.57 3.57a1 1 0 0 1-.25 1z"/></svg>01632 960 418</span>
      <span class="contact__item"><svg viewBox="0 0 24 24"><path d="M2 5h20v14H2z M3 6l9 7 9-7" /></svg>info@tkbellowsec.co.uk</span>
      <span class="contact__item"><svg viewBox="0 0 24 24"><circle cx="12" cy="12" r="10"/></svg>www.tkbellowsec.co.uk</span>
    </div>
  </article>
</section>

<!-- outer spread: back + front -->
<section class="scene scene--outer">
  <div class="spread">
    <div class="spread__slot">
      <article class="page back">
        <div class="photo photo--townhouse" role="img" aria-label="Red brick period townhouse"></div>
        <div class="photo photo--glass" role="img" aria-label="Large dark glazed window panels"></div>
        <div class="photo photo--office" role="img" aria-label="Modern white office building"></div>
        <div class="brand">
          <span class="brand__mark"></span>
          <div><div class="brand__name">TK Bellows</div><div class="brand__sub">Exterior Care Ltd</div><div class="brand__tel">Tel: 01632 960 418</div></div>
        </div>
        <div class="contact">
          <span class="contact__item"><svg viewBox="0 0 24 24"><path d="M6.6 10.8a15 15 0 0 0 6.6 6.6l2.2-2.2a1 1 0 0 1 1-.25 11.4 11.4 0 0 0 3.6.57 1 1 0 0 1 1 1V20a1 1 0 0 1-1 1A17 17 0 0 1 3 4a1 1 0 0 1 1-1h3.5a1 1 0 0 1 1 1c0 1.25.2 2.45.57 3.57a1 1 0 0 1-.25 1z"/></svg>01632 960 418</span>
          <span class="contact__item"><svg viewBox="0 0 24 24"><path d="M2 5h20v14H2z"/></svg>info@tkbellowsec.co.uk</span>
          <span class="contact__item"><svg viewBox="0 0 24 24"><circle cx="12" cy="12" r="10"/></svg>www.tkbellowsec.co.uk</span>
        </div>
      </article>
    </div>
    <div class="spread__slot">
      <article class="page front">
        <div class="brand">
          <span class="brand__mark"></span>
          <div><div class="brand__name">TK Bellows</div><div class="brand__sub">Exterior Care Ltd</div><div class="brand__tel">Tel: 01632 960 418</div></div>
        </div>
        <h1 class="headline">T.K Bellows Exterior Care is Southport's most reliable, professional cleaning company</h1>
        <div class="photo photo--shopfront" role="img" aria-label="Operative cleaning the glass frontage of a shop with a water fed pole"></div>
        <div class="services">
          <h2 class="section-title">Our services</h2>
          <ul class="services__list">
            <li>Window &amp; conservatory cleaning</li>
            <li>Roof cleaning &amp; treatment</li>
            <li>Render cleaning &amp; treatment</li>
            <li>Pressure washing</li>
            <li>Soft washing</li>
            <li>Gutter clearing</li>
            <li>Pressure washing of patios</li>
            <li>Driveways</li>
            <li>Gutters</li>
            <li>Fascias</li>
          </ul>
        </div>
        <div class="contact">
          <span class="contact__item"><svg viewBox="0 0 24 24"><path d="M6.6 10.8a15 15 0 0 0 6.6 6.6l2.2-2.2a1 1 0 0 1 1-.25 11.4 11.4 0 0 0 3.6.57 1 1 0 0 1 1 1V20a1 1 0 0 1-1 1A17 17 0 0 1 3 4a1 1 0 0 1 1-1h3.5a1 1 0 0 1 1 1c0 1.25.2 2.45.57 3.57a1 1 0 0 1-.25 1z"/></svg>01632 960 418</span>
          <span class="contact__item"><svg viewBox="0 0 24 24"><path d="M2 5h20v14H2z"/></svg>info@tkbellowsec.co.uk</span>
          <span class="contact__item"><svg viewBox="0 0 24 24"><circle cx="12" cy="12" r="10"/></svg>www.tkbellowsec.co.uk</span>
        </div>
      </article>
    </div>
  </div>
</section>

<!-- inner spread -->
<section class="scene scene--inner">
  <div class="spread">
    <div class="spread__slot">
      <article class="page about">
        <div class="photo photo--interior" role="img" aria-label="Warmly lit interior of a large commercial building"></div>
        <h2 class="section-title">About us</h2>
        <div class="body-copy body-copy--col">
          <p>T.K Bellows Exterior Care is a Southport based family business, serving homes and businesses across the North West for over ten years.</p>
          <p>At T.K Bellows we pride ourselves on reliable, friendly service. Every job is carried out by trained, insured staff using modern water fed pole systems and safe low pressure methods.</p>
          <p>Whether it is a single conservatory or a large commercial site, we plan each visit carefully so your property is left spotless and protected.</p>
        </div>
        <div class="body-copy body-copy--wide">
          <p>We like to keep things simple: one call, a clear quote and a regular visit that fits around you. From small terraced homes to offices, schools and retail units, we tailor each clean to the building.</p>
          <p>Our team is fully insured and happy to talk through any job. Please see the services page of our website for more detail.</p>
        </div>
      </article>
    </div>
    <div class="spread__slot">
      <article class="page detail">
        <h2 class="section-title">Lorem ipsum</h2>
        <div class="body-copy body-copy--col">
          <p>Soft washing uses gentle pressure and safe cleaning solutions to lift moss, algae and lichen from roofs and render without damage to the surface.</p>
          <p>Driveways and block paving are cleaned with rotary surface tools, then re-sanded and sealed on request for a lasting finish.</p>
          <p>Gutters are cleared and flushed using vacuum systems with camera checks, so blockages are found and fixed fast.</p>
        </div>
        <div class="photo photo--van" role="img" aria-label="White company van parked outside a property"></div>
        <div class="photo photo--van-dark" role="img" aria-label="Company van on a driveway"></div>
        <div class="photo photo--facade" role="img" aria-label="Tall glazed building facade being cleaned from ground level"></div>
      </article>
    </div>
  </div>
</section>

<!-- back cover -->
<section class="scene scene--back">
  <article class="page back">
    <div class="photo photo--townhouse" role="img" aria-label="Red brick period townhouse"></div>
    <div class="photo photo--glass" role="img" aria-label="Large dark glazed window panels"></div>
    <div class="photo photo--office" role="img" aria-label="Modern white office building"></div>
    <div class="brand">
      <span class="brand__mark"></span>
      <div><div class="brand__name">TK Bellows</div><div class="brand__sub">Exterior Care Ltd</div><div class="brand__tel">Tel: 01632 960 418</div></div>
    </div>
    <div class="contact">
      <span class="contact__item"><svg viewBox="0 0 24 24"><path d="M6.6 10.8a15 15 0 0 0 6.6 6.6l2.2-2.2a1 1 0 0 1 1-.25 11.4 11.4 0 0 0 3.6.57 1 1 0 0 1 1 1V20a1 1 0 0 1-1 1A17 17 0 0 1 3 4a1 1 0 0 1 1-1h3.5a1 1 0 0 1 1 1c0 1.25.2 2.45.57 3.57a1 1 0 0 1-.25 1z"/></svg>01632 960 418</span>
      <span class="contact__item"><svg viewBox="0 0 24 24"><path d="M2 5h20v14H2z"/></svg>info@tkbellowsec.co.uk</span>
      <span class="contact__item"><svg viewBox="0 0 24 24"><circle cx="12" cy="12" r="10"/></svg>www.tkbellowsec.co.uk</span>
    </div>
  </article>
</section>

</body>
</html>
```